Menu Cover Design

Need a menu cover design for a cafe/restaurant featuring the logo with Australian theme and the word MENU.
Menu size is A3 with saddle stitched binding.
No restriction to the colour scheme, but will be good if can use red/black/white. The look and feel should be clean cut buy yet casual/fun.
Visit www.pelbury.com.sg (Pelbury Cafe) for better understanding of the business.
Attached the logo file, the two mad faces (optional to use) and the current cover design for your reference.
Final deliverables: Working file AI/PSD, font files & JPEG.

```html
<!DOCTYPE html>
<html lang="en">
<head>
<meta charset="utf-8">
<title>Pelbury Cafe – Menu Cover</title>
<link rel="stylesheet" href="https://fonts.googleapis.com/css2?family=Krona+One&family=Michroma&family=Oswald:wght@500&display=swap">
<style>
  :root {
    --red: #e8140f;
    --red-mid: #f0504b;
    --red-soft: #f8aeab;
    --black: #1c1c1c;
    --charcoal: #2a2a2a;
    --grey: #8c8d8f;
    --white: #ffffff;
  }
  html, body {
    margin: 0;
    padding: 0;
    overflow: hidden;
    background: var(--white);
  }
  .cover {
    position: relative;
    width: 849px;
    height: 1200px;
    overflow: hidden;
    background: var(--white);
  }
  .art {
    position: absolute;
    background: radial-gradient(ellipse at 50% 45%, var(--red) 0%, var(--red-mid) 45%, var(--red-soft) 85%, #fde3e2 100%);
  }
  .art--top {
    left: -10px;
    top: -10px;
    width: 555px;
    height: 470px;
    border-radius: 0 30% 48% 42% / 0 30% 44% 40%;
  }
  .art--bottom {
    left: 345px;
    top: 748px;
    width: 520px;
    height: 470px;
    border-radius: 44% 0 0 0 / 40% 0 0 0;
  }
  .art--boomerang {
    left: 50px;
    top: 575px;
    width: 105px;
    height: 115px;
    background: linear-gradient(160deg, #3a3a3a 0%, var(--charcoal) 100%);
    border-radius: 70% 20% 40% 30% / 30% 20% 70% 60%;
  }
  .brand-name {
    position: absolute;
    left: 88px;
    top: 470px;
    width: 694px;
    margin: 0;
    font-family: "Krona One", sans-serif;
    font-size: 74px;
    line-height: 84px;
    color: var(--red);
    text-align: right;
    letter-spacing: 10px;
    margin-right: -10px;
  }
  .tagline {
    position: absolute;
    left: 150px;
    top: 566px;
    width: 632px;
    margin: 0;
    font-family: "Michroma", sans-serif;
    font-size: 24px;
    line-height: 30px;
    color: var(--black);
    text-align: right;
    letter-spacing: 3px;
    white-space: nowrap;
  }
  .promises {
    position: absolute;
    left: 170px;
    top: 605px;
    width: 612px;
    height: 22px;
    margin: 0;
    padding: 0 8px;
    box-sizing: border-box;
    list-style: none;
    display: flex;
    justify-content: space-between;
    align-items: center;
    background: var(--red);
    font-family: "Oswald", sans-serif;
    font-weight: 500;
    font-size: 14px;
    color: var(--white);
    letter-spacing: 0.3px;
  }
  .promises li + li::before {
    content: "|";
    margin-right: 8px;
  }
  .menu-word {
    position: absolute;
    left: 186px;
    top: 620px;
    margin: 0;
    font-family: "Krona One", sans-serif;
    font-size: 134px;
    line-height: 140px;
    color: var(--grey);
    letter-spacing: -3px;
    transform: scaleX(1.22);
    transform-origin: left center;
  }
</style>
</head>
<body>
  <main class="cover">
    <div class="art art--top" role="img" aria-label="Hand-drawn red outline character doodle with spiral eyes and toothy grin"></div>

    <h1 class="brand-name">PELBURY</h1>
    <div class="art art--boomerang" role="img" aria-label="Black boomerang with cartoon cuss symbols"></div>
    <p class="tagline">FRESH &amp; TASTY AUSSIE GRUB</p>
    <ul class="promises">
      <li>NO MSG</li>
      <li>5&#9733; INGREDIENTS</li>
      <li>CRAZY VALUE</li>
      <li>VARIETY</li>
      <li>MONEY-BACK GUARANTEE</li>
    </ul>
    <h2 class="menu-word">menu</h2>

    <div class="art art--bottom" role="img" aria-label="Hand-drawn red outline wild-haired character doodle with wide eyes and clenched teeth"></div>
  </main>
</body>
</html>
```